Plumvale CEO needs a Crowdsourced Graphic for a Wirelark Article

I need a simple graphic / banner for a blog post that's going to be posted on Wirelark (www.wirelark.com) - the biggest tech blog in the world.

The article will be written by Tobin Marsh (Plumvale's CEO) and the title will be "Asia's Secret Crowdsourcing Boom". The article is about the tens of thousands of people using crowdsourcing websites (like Plumvale.com, Qorvel.com and Vantrio.com) in China, India, the Philippines, Australia and other countries in the Asia Pacific region.

We'd really like to get this ASAP - so early submissions encouraged. We will try and get the winning designer linked to from the article.

Thanks to everyone that submitted!  Some great designs and hard to choose! :)

Target Market(s)

Tech saavy readers, English speakers

Industry/Entity Type

Tech

Requirements
Must have
• The graphic SHOULD:
1) Have the text "Asia's secret crowdsourcing boom" with some nice design and fonts (consider grey subtle pattern background and white drop shadow on fonts) - see attached examples
2) Have an Asian theme
3) Have the dimensions 640px wide by 240px wide
Nice to have
• The graphic COULD:
1) Have references to some or all of the countries mentioned above or use Asian characters as part of the background / motif (maybe the word "crowd" or "crowd sourcing" in different languages). In Chinese, the word for crowdsourcing is "witkey" (and there are corresponding Chinese characters: ??)
2) Emphasize the word "Asia" (using color and larger/different font)
3) Use a chart showing exponential (i.e. fast) growth - like the attached
4) Have a second line of text "5 Things You Didn't Know About Crowdsourcing in Asia"

```html
<!DOCTYPE html>
<html lang="en">
<head>
<meta charset="utf-8">
<title>Asia's Secret Crowdsourcing Boom</title>
<link href="https://fonts.googleapis.com/css2?family=Yeseva+One&family=Arimo:wght@400;700&display=swap" rel="stylesheet">
<style>
  :root {
    --bg: #efefee;
    --bg-dot: #e2e2e0;
    --magenta: #b2288f;
    --teal: #1fb3c6;
    --ink: #1a1a1a;
    --white: #ffffff;
  }
  html, body {
    margin: 0;
    padding: 0;
    width: 1200px;
    height: 450px;
    overflow: hidden;
  }
  .banner {
    position: relative;
    width: 1200px;
    height: 450px;
    overflow: hidden;
    background-color: var(--bg);
    background-image: radial-gradient(var(--bg-dot) 1px, transparent 1.4px);
    background-size: 5px 5px;
  }
  .headline {
    position: absolute;
    left: 36px;
    top: 14px;
    margin: 0;
    font-weight: normal;
  }
  .headline-asia {
    font-family: "Yeseva One", Georgia, serif;
    font-size: 104px;
    line-height: 1;
    color: var(--magenta);
    letter-spacing: 1px;
    text-shadow: 2px 2px 0 var(--white);
  }
  .headline-secret {
    font-family: "Arimo", Arial, sans-serif;
    font-size: 74px;
    color: var(--ink);
    margin-left: 14px;
    letter-spacing: -1px;
    text-shadow: 2px 2px 0 var(--white);
  }
  .headline-sub {
    display: block;
    font-family: "Arimo", Arial, sans-serif;
    font-size: 50px;
    line-height: 1;
    color: var(--teal);
    margin-top: 0;
    margin-left: 10px;
    text-shadow: 2px 2px 0 var(--white);
  }
  .growth-chart {
    position: absolute;
    left: 0;
    top: 0;
    width: 1200px;
    height: 450px;
  }
  .chart-marker-label {
    font-family: "Arimo", Arial, sans-serif;
    font-weight: 700;
    font-size: 20px;
    fill: var(--teal);
  }
  .crowd-circle {
    position: absolute;
    left: 810px;
    top: 25px;
    width: 300px;
    height: 300px;
    border-radius: 50%;
    background: radial-gradient(circle, #2a7fb5 0 18%, #f3e6ea 19% 52%, #e7c9d6 53% 100%);
  }
  .subtitle-band {
    position: absolute;
    left: 0;
    top: 386px;
    width: 1200px;
    height: 48px;
    background: var(--teal);
    display: flex;
    align-items: center;
    padding-left: 16px;
    box-sizing: border-box;
  }
  .subtitle-number {
    width: 34px;
    height: 34px;
    border-radius: 50%;
    background: var(--white);
    color: var(--teal);
    font-family: "Arimo", Arial, sans-serif;
    font-weight: 700;
    font-size: 26px;
    display: flex;
    align-items: center;
    justify-content: center;
    margin-right: 12px;
  }
  .subtitle-text {
    font-family: "Arimo", Arial, sans-serif;
    font-size: 29px;
    color: var(--white);
    margin: 0;
    font-weight: normal;
  }
</style>
</head>
<body>
<div class="banner">
  <h1 class="headline">
    <span class="headline-asia">ASIA'S</span><span class="headline-secret">Secret</span>
    <span class="headline-sub">crowdsourcing boom</span>
  </h1>

  <svg class="growth-chart" viewBox="0 0 1200 450" aria-label="Growth chart rising across five steps">
    <defs>
      <pattern id="bar-stripes" width="20" height="450" patternUnits="userSpaceOnUse">
        <rect x="8" y="0" width="2.5" height="450" fill="#b2288f"/>
      </pattern>
    </defs>
    <polygon class="chart-bars" fill="url(#bar-stripes)"
      points="38,375 150,347 262,328 347,285 469,262 632,221 722,182 722,386 38,386"/>
    <polyline class="chart-line" fill="none" stroke="#1fb3c6" stroke-width="4" stroke-linejoin="round"
      points="38,375 150,347 262,328 347,285 469,262 632,221 722,182"/>
    <g class="chart-markers">
      <circle cx="150" cy="347" r="14" fill="#fff" stroke="#1fb3c6" stroke-width="4"/>
      <text class="chart-marker-label" x="150" y="354" text-anchor="middle">1</text>
      <circle cx="262" cy="328" r="14" fill="#fff" stroke="#1fb3c6" stroke-width="4"/>
      <text class="chart-marker-label" x="262" y="335" text-anchor="middle">2</text>
      <circle cx="347" cy="285" r="14" fill="#fff" stroke="#1fb3c6" stroke-width="4"/>
      <text class="chart-marker-label" x="347" y="292" text-anchor="middle">3</text>
      <circle cx="469" cy="262" r="14" fill="#fff" stroke="#1fb3c6" stroke-width="4"/>
      <text class="chart-marker-label" x="469" y="269" text-anchor="middle">4</text>
      <circle cx="632" cy="221" r="14" fill="#fff" stroke="#1fb3c6" stroke-width="4"/>
      <text class="chart-marker-label" x="632" y="228" text-anchor="middle">5</text>
    </g>
  </svg>

  <div class="crowd-circle" role="img" aria-label="Illustration of eight people in colourful Asian dress arranged in a ring around a blue crowd emblem"></div>

  <div class="subtitle-band">
    <span class="subtitle-number">5</span>
    <h2 class="subtitle-text">Things You Didn’t Know About Crowdsourcing in Asia</h2>
  </div>
</div>
</body>
</html>
```